quorvadeal.com redesign with wireframes, white space and custom form are very important

Need a new two column design that will convert easily to mobile responsive. Lots of white space. Winning design will probably be based on header area and making the custom form stand out. I want the header to be very much like www.talbekmo.com except the form not to go up into the header.
Here are some of the websites I really like:
www.pivrostacks.com
http://glendarokfastmove.com/
http://morquilandestate.com/

We buy homes for cash and close fast. Our target is a home seller who is desperate to sell quickly.
I have uploaded my really ugly wireframe and my logo. I also uploaded my photo for the about us box and a possible photo to use for the header.
The copy on the wireframe is what I will be using except for the about us box.

Here is the exact link for video to frame in the top left box.
https://example-vidhost.net/Kp39xqTzR2a

Number of Pages Required

1 page

Font styles to use
Sans Serif

Colors
0592cd
85cae6
eaf1f7
fbee3d
ec1f27

Requirements
Must have
• Everything on wireframe.
• Must use Verdana font and nothing should be smaller than 12 point. Most should be in 14 point. (except maybe inside of form)

```html
<!DOCTYPE html>
<html lang="en">
<head>
<meta charset="utf-8">
<title>Quorvadeal — Sell Your Home Fast</title>
<link rel="stylesheet" href="https://fonts.googleapis.com/css2?family=Open+Sans:ital,wght@0,400;0,600;0,700;1,400&display=swap">
<style>
:root{
  --blue:#0592cd;
  --light-blue:#85cae6;
  --pale:#eaf1f7;
  --yellow:#fbee3d;
  --field:#fbf4a0;
  --red:#ec1f27;
  --orange-red:#ef4a2a;
  --text:#444;
  --muted:#666;
  --band:#e9ecef;
  --box:#dfe3e7;
  --page:#f4f6f8;
  --footer:#2f2f2f;
  --footer-bar:#1f1f1f;
}
*{box-sizing:border-box;margin:0;padding:0}
html,body{width:1200px;height:3005px;overflow:hidden}
body{font-family:"Open Sans",Verdana,sans-serif;color:var(--text);background:var(--page);position:relative}
.abs{position:absolute}
/* header */
.site-header{left:0;top:0;width:1200px;height:142px;background:#fff}
.brand{left:130px;top:40px;font-weight:700;font-size:34px;color:var(--red);letter-spacing:-.5px}
.call-line{right:134px;top:16px;font-size:14px;color:#555;letter-spacing:.5px}
.call-line span{color:var(--red)}
.phone{right:134px;top:38px;font-size:20px;color:#444;display:flex;align-items:center;gap:10px}
.main-nav{left:362px;top:110px;display:flex;gap:30px;font-size:13px;font-weight:600;color:#444;text-transform:uppercase}
.main-nav .active{color:var(--blue)}
/* hero */
.hero{left:0;top:142px;width:1200px;height:468px;background:linear-gradient(180deg,#7f9a62 0%,#8b8d6c 35%,#6d6f55 70%,#4f6b38 100%)}
.caption-dark{left:130px;top:362px;width:382px;height:40px;background:#111;color:#fff;font-size:21px;padding:4px 14px}
.caption-red{left:130px;top:418px;width:328px;height:42px;background:var(--orange-red);color:#fff;font-size:21px;font-weight:600;padding:5px 14px}
.dots{left:132px;top:588px;display:flex;gap:6px}
.dots i{width:12px;height:12px;border-radius:50%;background:#fff;display:block}
.dots i:first-child{background:var(--red)}
/* form */
.lead-form{left:618px;top:544px;width:448px;height:590px;background:var(--yellow)}
.lead-form header{height:66px;background:var(--blue);color:#fff;text-align:center;padding-top:8px}
.lead-form h2{font-size:22px;font-weight:700}
.lead-form p{font-size:13px}
.field{margin:20px 20px 0;height:40px;background:var(--field);border:1px solid #f3e26a;border-radius:4px;font-size:12px;color:#666;display:flex;align-items:center;gap:10px;padding-left:12px}
.field+.field{margin-top:22px}
.field svg{flex:none}
.submit{margin:28px 20px 0;height:50px;background:var(--orange-red);color:#fff;border-radius:4px;font-size:16px;font-weight:600;display:flex;align-items:center;justify-content:center}
/* left column */
h3.section-title{color:var(--blue);font-size:23px;font-weight:600;line-height:1.4}
.ticks{list-style:none;font-size:14px;color:#444}
.ticks li{display:flex;align-items:center;gap:12px;height:30px}
.ticks.bold li{font-weight:600;font-size:14px}
.video{left:138px;top:866px;width:436px;height:268px;background:#e9e9e9;border:1px solid #ddd}
.video .frame{position:absolute;left:4px;top:4px;width:426px;height:226px;background:linear-gradient(135deg,#8cb45a,#c9d8b0 55%,#e6d2bf 80%,#d4b8a2)}
.video .controls{position:absolute;left:4px;bottom:6px;width:426px;height:28px;display:flex;align-items:center;gap:10px;padding:0 10px;font-size:10px;color:#555}
.video .bar{flex:1;height:4px;background:#444}
/* band */
.band{left:0;top:1170px;width:1200px;height:648px;background:var(--band)}
.band-copy{font-size:14px;line-height:1.75;color:#555}
.card{background:var(--box)}
.btn-red{background:var(--orange-red);color:#fff;font-size:16px;font-weight:600;border-radius:4px;display:flex;align-items:center;justify-content:center}
.social-sq{width:48px;height:48px;border-radius:4px;background:var(--blue)}
.card h4{color:var(--blue);font-size:23px;font-weight:400}
.quote{font-style:italic;font-size:13px;line-height:1.7;color:#555}
.portrait{background:linear-gradient(160deg,#9fb9d6,#c9a48c 60%,#4a6b98)}
/* blog */
.blog-item{left:130px;width:450px;height:104px}
.blog-item .thumb{position:absolute;left:0;top:0;width:84px;height:84px;background:linear-gradient(160deg,#f1f1f1,#c9a58a 60%,#6e86a8)}
.blog-item h5{position:absolute;left:106px;top:0;color:var(--blue);font-size:14px;font-weight:600}
.blog-item time{position:absolute;right:0;top:2px;color:var(--red);font-size:11px}
.blog-item p{position:absolute;left:106px;top:22px;width:344px;font-size:13px;line-height:1.65;color:#444}
.cities{left:618px;top:1862px;width:448px;height:484px;background:var(--box);padding:20px 20px}
.cities p{font-size:13px;line-height:1.85;color:#666;letter-spacing:.2px}
/* showcase */
.showcase{left:130px;top:2382px;width:936px;height:196px;background:var(--box)}
.house-photo{position:absolute;top:18px;width:212px;height:162px}
/* footer */
.footer-brand{left:0;top:2622px;width:1200px;text-align:center;font-size:34px;font-weight:700;color:var(--red);letter-spacing:-.5px}
.footer{left:0;top:2700px;width:1200px;height:260px;background:var(--footer)}
.footer h6{position:absolute;color:#fff;font-size:16px;font-weight:600}
.link-list{list-style:none;font-size:12px;color:#ddd;line-height:22px}
.link-list li::before{content:"› ";color:#ddd}
.contact{font-size:12px;color:#ddd;line-height:20px}
.contact-lines{font-size:12px;color:#ddd;line-height:32px}
.follow{list-style:none;font-size:12px;color:#ddd}
.follow li{display:flex;align-items:center;gap:10px;height:34px}
.follow i{width:20px;height:20px;background:#eee;display:block;border-radius:2px}
.legal{left:0;top:2960px;width:1200px;height:45px;background:var(--footer-bar);color:#ccc;font-size:11px}
</style>
</head>
<body>

<header class="abs site-header">
  <div class="abs brand">quorvadeal.com</div>
  <div class="abs call-line">CALL US &nbsp;<span>NIGHTS AND WEEKENDS OK</span></div>
  <div class="abs phone">
    <svg width="20" height="22" viewBox="0 0 20 22"><path d="M4 1l4 5-2 3c1 3 4 6 7 7l3-2 4 4-3 3C9 20 1 12 1 4z" fill="#ec1f27"/></svg>
    407-555-0142
  </div>
  <nav class="abs main-nav">
    <span class="active">Home</span><span>About</span><span>Sell your home</span><span>How it works</span><span>Stop foreclosure</span><span>Probate</span><span>Contact us</span>
  </nav>
</header>

<section class="abs hero" role="img" aria-label="Craftsman style two-storey house with green siding, brick chimney and a garden in front"></section>
<div class="abs caption-dark">Sell your home for cash in 8 days</div>
<div class="abs caption-red">We buy Houses Nationwide.</div>
<div class="abs dots"><i></i><i></i><i></i></div>

<form class="abs lead-form">
  <header><h2>YES, I WANT TO SELL MY HOME FAST!</h2><p>Get a no obligation written offer in 36 hours</p></header>
  <div class="field"><svg width="12" height="12"><circle cx="6" cy="4" r="3" fill="#777"/><rect x="1" y="8" width="10" height="4" rx="2" fill="#777"/></svg>Your Name</div>
  <div class="field"><svg width="12" height="12"><rect x="1" y="3" width="10" height="8" rx="1" fill="#777"/></svg>Your phone number</div>
  <div class="field"><svg width="12" height="12"><rect x="0" y="2" width="12" height="8" fill="#777"/></svg>Your Email Address</div>
  <div class="field"><svg width="12" height="12"><rect x="1" y="1" width="10" height="10" fill="none" stroke="#777" stroke-width="2"/></svg>Address including City, State &amp; Zip Code</div>
  <div class="field"><svg width="12" height="12"><circle cx="6" cy="6" r="4" fill="none" stroke="#777" stroke-width="3"/></svg>Repairs needed if any</div>
  <div class="field"><svg width="12" height="12"><path d="M1 6l5-5h5v5l-5 5z" fill="#777"/></svg>Asking price</div>
  <div class="field"><svg width="12" height="12"><rect x="1" y="2" width="10" height="7" fill="#777"/></svg>Comments</div>
  <div class="submit">Submit, to get started selling your home fast.</div>
</form>

<h3 class="abs section-title" style="left:130px;top:632px">Benefits of selling your home to us</h3>
<ul class="abs ticks" style="left:132px;top:682px">
  <li><svg width="18" height="18"><rect x="1" y="3" width="13" height="13" fill="none" stroke="#888"/><path d="M4 9l3 3 8-10" fill="none" stroke="#444" stroke-width="2"/></svg>You pick the closing date</li>
  <li><svg width="18" height="18"><rect x="1" y="3" width="13" height="13" fill="none" stroke="#888"/><path d="M4 9l3 3 8-10" fill="none" stroke="#444" stroke-width="2"/></svg>You pay NO commissions or fees</li>
  <li><svg width="18" height="18"><rect x="1" y="3" width="13" height="13" fill="none" stroke="#888"/><path d="M4 9l3 3 8-10" fill="none" stroke="#444" stroke-width="2"/></svg>You don't have to paint, clean or make repairs</li>
</ul>
<h3 class="abs section-title" style="left:134px;top:792px;width:450px">Watch to see our president Marlo explain how easy it is to sell to us</h3>
<div class="abs video">
  <div class="frame" role="img" aria-label="Video still of a hand holding a small model house"></div>
  <div class="controls"><svg width="10" height="10"><path d="M1 0l8 5-8 5z" fill="#333"/></svg>02:00/00:03<span class="bar"></span><svg width="12" height="10"><path d="M0 3h3l4-3v10l-4-3H0z" fill="#333"/></svg><span style="width:40px;height:4px;background:#444"></span></div>
</div>

<div class="abs band"></div>
<h3 class="abs section-title" style="left:134px;top:1200px;width:450px">Sell your home or house fast for cash to a professional investor company. We buy Housesand close quickly.</h3>
<p class="abs band-copy" style="left:134px;top:1312px;width:440px">Selling a home on your own has never been easier. From Orlando to Greensboro - and all points in between- you can sell your home today without any hassles. Call 1-800-555-0199 or fill out the form below to get a written offer on your home in just 36 hours. Sell today online to people that care.</p>
<h3 class="abs section-title" style="left:134px;top:1458px">If you need to sell a home fast because of</h3>
<ul class="abs ticks bold" style="left:134px;top:1506px">
  <li><svg width="18" height="18"><rect x="1" y="3" width="13" height="13" fill="none" stroke="#888"/><path d="M4 9l3 3 8-10" fill="none" stroke="#444" stroke-width="2"/></svg>Divorce or Bankruptcy</li>
  <li><svg width="18" height="18"><rect x="1" y="3" width="13" height="13" fill="none" stroke="#888"/><path d="M4 9l3 3 8-10" fill="none" stroke="#444" stroke-width="2"/></svg>Foreclosure</li>
  <li><svg width="18" height="18"><rect x="1" y="3" width="13" height="13" fill="none" stroke="#888"/><path d="M4 9l3 3 8-10" fill="none" stroke="#444" stroke-width="2"/></svg>Landlord problems - evictions with tenants okay</li>
  <li><svg width="18" height="18"><rect x="1" y="3" width="13" height="13" fill="none" stroke="#888"/><path d="M4 9l3 3 8-10" fill="none" stroke="#444" stroke-width="2"/></svg>Inherited property in probate</li>
  <li><svg width="18" height="18"><rect x="1" y="3" width="13" height="13" fill="none" stroke="#888"/><path d="M4 9l3 3 8-10" fill="none" stroke="#444" stroke-width="2"/></svg>Termites, mold, flood or fire damage, leaky roof</li>
  <li><svg width="18" height="18"><rect x="1" y="3" width="13" height="13" fill="none" stroke="#888"/><path d="M4 9l3 3 8-10" fill="none" stroke="#444" stroke-width="2"/></svg>Moving or can't afford mortgage payments</li>
</ul>
<h3 class="abs section-title" style="left:134px;top:1720px">We Can Help.<br>We are the fastest home buyers around.</h3>

<div class="abs card" style="left:618px;top:1196px;width:448px;height:86px"></div>
<div class="abs btn-red" style="left:636px;top:1216px;width:190px;height:48px">Our Privacy Policy</div>
<div class="abs social-sq" style="left:862px;top:1214px"></div>
<div class="abs social-sq" style="left:928px;top:1214px"></div>
<div class="abs social-sq" style="left:994px;top:1214px;background:#6b6f73"></div>
<div class="abs card" style="left:618px;top:1302px;width:448px;height:60px;display:flex;align-items:center;justify-content:center;color:var(--blue);font-size:14px;font-weight:600">Call us 8am to 10 pm Eastern time. We answer our phones.</div>
<div class="abs card" style="left:618px;top:1384px;width:448px;height:140px;padding:12px 22px">
  <h4>Home Seller Testimonials</h4>
  <p class="quote" style="margin-top:10px">I just wanted to thank you for buying my home in Winter Park. You made it fast and easy and kept me well informed the whole way.</p>
</div>
<svg class="abs" style="left:980px;top:1522px" width="40" height="34"><path d="M0 0h40L0 34z" fill="#dfe3e7"/></svg>
<div class="abs" style="left:618px;top:1526px;font-size:13px;font-weight:600;color:var(--red);text-decoration:underline">Read More</div>
<div class="abs" style="left:766px;top:1526px;font-size:13px;font-style:italic;font-weight:600;color:#555">Dessa Kornfeld – Winter Park</div>
<div class="abs card" style="left:618px;top:1574px;width:448px;height:206px;padding:14px 22px">
  <h4>About Us</h4>
  <div class="abs portrait" role="img" aria-label="Portrait photo of the company owner" style="left:20px;top:54px;width:116px;height:138px;border:3px solid #fff"></div>
  <p class="abs quote" style="left:156px;top:52px;width:270px">Owned and operated in Orlando Florida since 2001. Oldest Continuous operated website in country.</p>
</div>

<h3 class="abs" style="left:130px;top:1846px;font-size:22px;font-weight:600;color:var(--blue)">Latest <span style="color:var(--red)">Blog</span></h3>
<div class="abs" style="left:130px;top:1886px;width:450px;height:3px;background:#333"></div>
<div class="abs blog-item" style="top:1910px"><div class="thumb" role="img" aria-label="Blog author photo"></div><h5>Vlandit Pnt Luatum Zril</h5><time>02 May 2015</time><p>Lorem ipsum dolor smit amet consectetuer euism od magni aliquam erat volutpat. Ut wisi enim ad minim r suscipit lobortis [...]</p></div>
<div class="abs blog-item" style="top:2024px"><div class="thumb" role="img" aria-label="Blog author photo"></div><h5>Vlandit Pnt Luatum Zril</h5><time>02 May 2015</time><p>Lorem ipsum dolor smit amet consectetuer euism od magni aliquam erat volutpat. Ut wisi enim ad minim r suscipit lobortis [...]</p></div>
<div class="abs blog-item" style="top:2138px"><div class="thumb" role="img" aria-label="Blog author photo"></div><h5>Vlandit Pnt Luatum Zril</h5><time>02 May 2015</time><p>Lorem ipsum dolor smit amet consectetuer euism od magni aliquam erat volutpat. Ut wisi enim ad minim r suscipit lobortis [...]</p></div>
<div class="abs blog-item" style="top:2252px"><div class="thumb" role="img" aria-label="Blog author photo"></div><h5>Vlandit Pnt Luatum Zril</h5><time>02 May 2015</time><p>Lorem ipsum dolor smit amet consectetuer euism od magni aliquam erat volutpat. Ut wisi enim ad minim r suscipit lobortis [...]</p></div>

<div class="abs cities">
  <h3 class="section-title" style="font-size:22px;margin-bottom:18px">Some of the cities where we buy houses. Not all are listed.</h3>
  <p>These are the cities where we have an affiliate where you can sell a home fast for quickly and we buy homes: Orlando Jacksonville Ft Myers Tampa St Pete Gainesville Tallahassee Melbourne West Palm Beach Apopka Deland Kissimmee Lakeland Ocala Chicago Philadelphia Camden Atlanta Valdosta Houston Detroit Phoenix Seattle Tacoma Portland Charlotte Cincinnati San Antonio Harrisburg Virginia Beach Virginia Homes Greensboro Charleston SC Flint Rochester Lake Florida Wilmington Columbia Titusville If you don't see your city, we still probably buy homes there.</p>
  <p style="margin-top:16px">These are the types of real estate that we buy: We buy nice houses and outdated problem homes. We buy in great neighborhoods and not so nice. We buy block homes and frame homes. We buy</p>
</div>

<div class="abs showcase">
  <div class="house-photo" role="img" aria-label="Single-storey house with lawn and trees" style="left:20px;background:linear-gradient(180deg,#5f8a3c,#c9c8bd 50%,#6f9a45)"></div>
  <div class="house-photo" role="img" aria-label="House with white garage door and driveway" style="left:242px;background:linear-gradient(180deg,#9ab9d8,#d6d4cc 50%,#8a8a82)"></div>
  <h3 class="abs section-title" style="left:500px;top:66px;width:420px;text-align:center">We buy nice pretty houses and some ugly ones as well.</h3>
</div>

<div class="abs footer-brand">quorvadeal.com</div>
<footer class="abs footer">
  <h6 style="left:134px;top:52px">Quick Links</h6>
  <div class="abs" style="left:134px;top:82px;width:180px;height:1px;background:#555"></div>
  <ul class="abs link-list" style="left:134px;top:92px">
    <li>Home</li><li>About</li><li>Sell Your Home</li><li>How it Works</li><li>Stop Foreclosure</li><li>Probate</li><li>Contact Us</li>
  </ul>
  <ul class="abs link-list" style="left:362px;top:92px">
    <li>Archives</li><li>Sell my house</li><li>Fast cash for homes</li><li>We buy houses</li><li>Real Estate investor</li><li>Latest</li>
  </ul>
  <h6 style="left:618px;top:52px">Contact Detail</h6>
  <div class="abs" style="left:618px;top:82px;width:190px;height:1px;background:#555"></div>
  <div class="abs contact" style="left:618px;top:92px"><b style="color:#fff">Quorvadeal</b><br>16 Lorem ipsum dolor sit amet<br>sed benetion, Street no-123456</div>
  <div class="abs contact-lines" style="left:618px;top:160px">☏&nbsp; 123-456-1789<br>☏&nbsp; 123-789-7890<br>✉&nbsp; info@quorvadeal.com</div>
  <h6 style="left:858px;top:52px">Follow Us</h6>
  <div class="abs" style="left:858px;top:82px;width:150px;height:1px;background:#555"></div>
  <ul class="abs follow" style="left:858px;top:86px"><li><i></i>Friendwall</li><li><i></i>Chirpline</li><li><i></i>Circlenet</li><li><i></i>Worklink</li></ul>
</footer>
<div class="abs legal"><span class="abs" style="left:134px;top:14px">Copyright © 2015 Quorvadeal . All Right Reserved.</span><span class="abs" style="right:134px;top:14px">Privacy Policy &nbsp;|&nbsp; Terms &amp; Conditions</span></div>

</body>
</html>
```